new product flyer for upcoming tradeshow sign up at the last minute

we are a start up manufacturer this year and this is our first product launch through a tradeshow on 11/7. The product category is Portable Gas Power Air Compressor; and within the category, there are two sub groups: Single Stage Gas Portable and 2Stage Gas Air Compressor.
Requirements: one main flyer that can fit all product detail illustrated with table, components, and photo.
two flyer one each for the sub group.

```html
<!DOCTYPE html>
<html lang="en">
<head>
<meta charset="utf-8">
<title>30-Gallon Truck Mount Series Flyer</title>
<link href="https://fonts.googleapis.com/css2?family=Poppins:wght@400;500;600;700;800&display=swap" rel="stylesheet">
<style>
  :root{
    --red-deep:#8c1018;
    --red:#c8161f;
    --red-bright:#e3202a;
    --yellow:#fff200;
    --navy:#1f2a6b;
    --white:#ffffff;
    --ink:#1b1b1b;
    --stage:#e9e9ea;
  }
  *{box-sizing:border-box;margin:0;padding:0}
  html,body{width:1200px;height:721px;overflow:hidden;background:var(--stage);font-family:"Poppins",sans-serif}
  .sheet{position:absolute;left:327px;top:8px;width:546px;height:706px;box-shadow:0 6px 22px rgba(0,0,0,.18)}
  .flyer{position:absolute;left:0;top:0;width:945px;height:1222px;transform:scale(.5778);transform-origin:0 0;color:var(--white);overflow:hidden;
    background:radial-gradient(ellipse at 45% 55%,var(--red-bright) 0%,var(--red) 35%,var(--red-deep) 100%)}
  .title{position:absolute;left:52px;top:38px;font-weight:800;color:var(--yellow);font-size:62px;line-height:52px;letter-spacing:-1px}
  .series{position:absolute;left:52px;top:168px;font-weight:800;font-size:47px;line-height:48px}
  .series small{display:block;font-size:28px;line-height:30px;font-weight:700}
  .intro{position:absolute;left:52px;top:270px;width:342px;font-size:12.3px;line-height:16px;font-weight:600;text-align:justify}
  .hero{position:absolute;left:405px;top:30px;width:500px;height:262px;border-radius:40px;
    background:radial-gradient(ellipse at 60% 55%,#5a5d63 0%,#34373c 45%,rgba(60,20,20,0) 72%)}
  .thumbs{position:absolute;left:430px;top:320px;display:flex;gap:8px}
  .thumb{width:108px;height:108px;border:4px solid var(--white);box-shadow:0 3px 8px rgba(0,0,0,.35)}
  .t1{background:linear-gradient(135deg,#9aa0a8,#4d535b)}
  .t2{background:linear-gradient(180deg,#8db6e0 0%,#c9a45a 45%,#b38631 100%)}
  .t3{background:linear-gradient(135deg,#dfe8f1,#7fa3c6)}
  .t4{background:linear-gradient(135deg,#c9d6e0,#6d8aa0)}
  .rule{position:absolute;left:52px;width:836px;border-top:1.5px dashed rgba(255,255,255,.75)}
  .vrule{position:absolute;top:462px;height:228px;border-left:1.5px dashed rgba(255,255,255,.75)}
  .specs{position:absolute;top:460px;font-size:12.5px;line-height:17px}
  .specs h3{font-size:12.5px;font-weight:700;margin:4px 0 5px}
  .specs h3+ul{margin-bottom:4px}
  .specs ul{list-style:none}
  .specs li{position:relative;padding-left:14px}
  .specs li::before{content:"✓";position:absolute;left:0;top:4px;width:9px;height:9px;border:1px solid var(--white);border-radius:50%;font-size:7px;line-height:8px;text-align:center}
  .units{position:absolute;left:735px;top:462px;width:170px;height:228px;border-radius:20px;
    background:radial-gradient(ellipse at 50% 30%,#44474c 0%,rgba(40,20,20,0) 60%),radial-gradient(ellipse at 50% 80%,#44474c 0%,rgba(40,20,20,0) 55%)}
  .group-title{position:absolute;left:50px;font-size:27px;font-weight:700;letter-spacing:.2px}
  table{position:absolute;left:44px;width:856px;border-collapse:collapse;table-layout:fixed;font-size:12.5px}
  col.c-model{width:117px} col.c-cfm{width:138px} col.c-engine{width:179px} col.c-pump{width:116px}
  col.c-psi{width:72px} col.c-dim{width:132px} col.c-weight{width:102px}
  th{height:24px;font-weight:500;font-size:12px;text-align:center;white-space:nowrap}
  th:nth-child(odd){background:var(--yellow);color:var(--ink)}
  th:nth-child(even){background:var(--navy);color:var(--white)}
  th:first-child{text-align:left;padding-left:6px}
  td{height:24.2px;text-align:center;white-space:nowrap;border-bottom:1px solid rgba(255,255,255,.45)}
  td:first-child{text-align:left;padding-left:6px}
  .footer{position:absolute;left:0;top:1097px;width:945px;height:125px;background:var(--white);color:var(--ink)}
  .brand{position:absolute;left:44px;top:42px;display:flex;align-items:center;gap:8px;color:var(--navy);font-weight:800;font-size:32px;letter-spacing:-.5px}
  .brand i{width:18px;height:18px;border-radius:50%;background:var(--navy)}
  .partner{position:absolute;left:322px;top:48px;font-weight:600;font-size:30px;color:var(--ink)}
  .badge{position:absolute;left:538px;top:14px;width:56px;height:56px;border-radius:50%;background:#d3d5dc;border:2px solid #9ea2ad}
  .warning{position:absolute;left:455px;top:72px;width:225px;text-align:center;font-size:9.5px;line-height:12px;font-weight:500}
  .warning b{color:var(--red)}
  .contact{position:absolute;right:43px;top:26px;text-align:right;font-size:13px;line-height:14px;font-weight:600}
  .contact .cta{display:block;margin-top:14px;color:var(--navy);font-weight:700}
  .contact .phone{display:block;color:var(--red);font-size:22px;line-height:24px;font-weight:700}
</style>
</head>
<body>
<div class="sheet">
  <div class="flyer">
    <h1 class="title">30-GALLON<br>TRUCK</h1>
    <h2 class="series">MOUNT SERIES<small>TWO STAGE GASOLINE</small></h2>
    <p class="intro">Introducing our powerful 30 Gallon Truck Mount Air Compressor Unit, a robust 2-stage air compressor designed for the toughest roadside emergency repairs. Whether you're dealing with semi tractor breakdowns or farm tractor maintenance, this unit delivers reliable, high performance air compression to get the job done efficiently. Its durable construction and easy mounting make it an essential tool for any mobile repair service, ensuring you're always prepared for any situation on the road.</p>
    <div class="hero" role="img" aria-label="Product photo: portable gas air compressors with pump head"></div>
    <div class="thumbs">
      <div class="thumb t1" role="img" aria-label="Photo: steel construction framework"></div>
      <div class="thumb t2" role="img" aria-label="Photo: tractor in a wheat field"></div>
      <div class="thumb t3" role="img" aria-label="Photo: laboratory equipment"></div>
      <div class="thumb t4" role="img" aria-label="Photo: technician at work"></div>
    </div>

    <div class="rule" style="top:453px"></div>
    <div class="vrule" style="left:336px"></div>
    <div class="vrule" style="left:722px"></div>

    <div class="specs" style="left:52px">
      <h3>COMPRESSOR PUMP</h3>
      <ul><li>Oversize cast iron compressor pump</li><li>Splash lubricated</li><li>Stainless-steel braided discharge hose</li><li>Large canister intake filter</li><li>Oil level sight indicator</li><li>Heavy-duty air filter</li><li>Oil level sight indicator</li></ul>
      <h3>LIMITED WARRANTY</h3>
      <ul><li>3year engine / 1 year pump exchange</li></ul>
      <h3>CERTIFICATIONS</h3>
      <ul><li>ASME</li></ul>
    </div>
    <div class="specs" style="left:364px">
      <h3>COMPONENTS</h3>
      <ul><li>Regulator and a gauges for tank and outlet pressure</li><li>ASME safety valves</li><li>16 1/2-inch fly wheel</li><li>Tank drain valve</li></ul>
      <h3>ENGINE</h3>
      <ul><li>Electric start</li><li>Automatic engine idle control (pneumatic)</li></ul>
      <h3>FRAME</h3>
      <ul><li>Powder coated ASME receiver tank</li><li>3/16-inch base plate to reduce vibration</li><li>Powder coated two-piece belt guard</li></ul>
    </div>
    <div class="units" role="img" aria-label="Product photos: two wheeled compressor units"></div>
    <div class="rule" style="top:693px"></div>

    <h2 class="group-title" style="top:710px">SINGLE STAGE - GASOLINE - PORTABLE</h2>
    <table style="top:752px">
      <colgroup><col class="c-model"><col class="c-cfm"><col class="c-engine"><col class="c-pump"><col class="c-psi"><col class="c-dim"><col class="c-weight"></colgroup>
      <thead><tr><th>MODEL NUMBER</th><th>OUTPUT CFM @ 90 PS</th><th>ENGINE INFO</th><th>PUMP INFO</th><th>PSI</th><th>UNIT DIMENSION</th><th>WEIGHT (LB)</th></tr></thead>
      <tbody>
        <tr><td>KH55-210</td><td>3.9</td><td>5.5HP HIRANO HR160</td><td>210</td><td>115</td><td>23.6 x 19.6 x 19.6"</td><td>78</td></tr>
        <tr><td>KK65-210</td><td>3.9</td><td>6.5HP KOLBE KB270</td><td>210</td><td>115</td><td>23.6 x 19.6 x 19.6"</td><td>82</td></tr>
        <tr><td>K1PH65-20R40</td><td>17</td><td>6.5HP HIRANO HR200</td><td>RB40 4HP/1</td><td>145</td><td>36.6x15x32.6</td><td>210</td></tr>
        <tr><td>KH55-10R40</td><td>17</td><td>5.5HP HIRANO HR160</td><td>RB40 4HP/1</td><td>145</td><td>44.5 x 20 x 27"</td><td>171</td></tr>
        <tr><td>KK65-10R40</td><td>17</td><td>6.5HP KOLBE KB270</td><td>RB40 4HP/1</td><td>145</td><td>44.5 x 20 x 27"</td><td>178</td></tr>
        <tr><td>KH13-10RB75</td><td>33</td><td>13HP HIRANO HR390</td><td>RB75 5HP/1</td><td>145</td><td>43 x 26 x 35"</td><td>270</td></tr>
      </tbody>
    </table>

    <h2 class="group-title" style="top:932px">TWO STAGE - GASOLINE - PORTABLE /TRUCK MOUNT</h2>
    <table style="top:974px">
      <colgroup><col class="c-model"><col class="c-cfm"><col class="c-engine"><col class="c-pump"><col class="c-psi"><col class="c-dim"><col class="c-weight"></colgroup>
      <thead><tr><th>MODEL NUMBER</th><th>OUTPUT CFM @ 90 PS</th><th>ENGINE INFO</th><th>PUMP INFO</th><th>PSI</th><th>UNIT DIMENSION</th><th>WEIGHT (LB)</th></tr></thead>
      <tbody>
        <tr><td>KK14-10KT05V</td><td>22</td><td>14HP KOLBE KB440</td><td>KT05V 5HP/2</td><td>175</td><td>43 x 26 x 35"</td><td>300</td></tr>
        <tr><td>KH13-10KT05V</td><td>22</td><td>13HP HIRANO HR390</td><td>KT05V 5HP/2</td><td>175</td><td>43 x 26 x 35"</td><td>300</td></tr>
        <tr><td>K2PH13-30KT05V</td><td>22</td><td>13HP HIRANO HR390</td><td>KT05V 5HP/2</td><td>175</td><td>42 x 22x 40"</td><td>426</td></tr>
      </tbody>
    </table>

    <footer class="footer">
      <div class="brand"><i></i>KESTREL AIR</div>
      <div class="partner">torvane</div>
      <div class="badge" role="img" aria-label="Assembled in USA badge"></div>
      <p class="warning"><b>WARNING:</b> Cancer and Reproductive Harm<br>www.safetynotice-info.org</p>
      <p class="contact">2480 Meridian Avenue,<br>Alder Park CA 90011<span class="cta">Call Now Today!</span><span class="phone">0040 5550 1288</span></p>
    </footer>
  </div>
</div>
</body>
</html>
```